Wordpress Redesign Project

Our website needs to become amazing. Because now it's not. The homepage especially does not actively convey what we do in an elegant way. We would want a minimalist redesign of www.plovK.com to look more like:

http://vantorelliworks.com/
http://www.quorvane.com/en-us/quorvaneflux.html
http://www.bramu.com/

It needs to work on Wordpress and be easily uploaded.

We also need an inside page of case studies (currently http://www.plovk.com/social-media-clients/) that plays the video in a larger pop-up screen .

Target Market(s)

Social Media Professionals, Creative and Advertising Agencies, Event marketing professionals

Industry/Entity Type

Media

```html
<!DOCTYPE html>
<html lang="en">
<head>
<meta charset="utf-8">
<title>plovK – Creating Brand Champions</title>
<link href="https://fonts.googleapis.com/css2?family=Ubuntu:wght@300;400;500;700&family=Open+Sans:wght@400;600&display=swap" rel="stylesheet">
<style>
  :root {
    --magenta: #e0117f;
    --magenta-light: #f0499f;
    --ink: #333;
    --text: #555;
    --muted: #8a8a8a;
    --line: #e3e3e3;
    --dark: #2b2b2b;
    --footer: #333333;
    --white: #fff;
  }
  * { box-sizing: border-box; margin: 0; padding: 0; }
  html, body { width: 799px; height: 1200px; overflow: hidden; background: var(--white); }
  body { position: relative; font-family: "Open Sans", sans-serif; color: var(--text); }
  .abs { position: absolute; }

  /* header */
  .brand { left: 52px; top: 20px; display: flex; align-items: center; gap: 8px; }
  .brand-mark { width: 40px; height: 40px; border-radius: 8px; background: var(--magenta); }
  .brand-name { font-family: "Ubuntu", sans-serif; font-weight: 700; font-size: 24px; color: var(--magenta); }
  .brand-rule { left: 184px; top: 33px; width: 1px; height: 32px; background: var(--line); }
  .tagline { left: 196px; top: 42px; font-family: "Ubuntu", sans-serif; font-weight: 300; font-size: 11px; color: var(--muted); }

  /* nav */
  .nav { left: 48px; top: 86px; width: 705px; height: 38px; display: flex;
         background: linear-gradient(#fbfbfb, #ececec); border: 1px solid #ddd; border-bottom: 3px solid var(--magenta); border-radius: 4px 4px 0 0; }
  .nav a { font-family: "Ubuntu", sans-serif; font-size: 13px; color: #555; text-decoration: none;
           padding: 0 17px; line-height: 35px; border-right: 1px solid #d8d8d8; }
  .nav a.active { background: linear-gradient(var(--magenta-light), var(--magenta)); color: var(--white); padding: 0 21px; border-radius: 3px 0 0 0; }

  /* hero */
  .hero { left: 47px; top: 134px; width: 705px; height: 242px; background: var(--dark); border-radius: 3px; overflow: hidden; }
  .hero-photo { position: absolute; left: 340px; top: 0; width: 365px; height: 242px;
                background: radial-gradient(circle at 55% 55%, #c9a48a, #6e5448 55%, #3a302c); }
  .hero-kicker { position: absolute; left: 42px; top: 32px; font-family: "Ubuntu", sans-serif; font-weight: 300; font-size: 24px; color: var(--white); }
  .hero-title { position: absolute; left: 42px; top: 60px; font-family: "Ubuntu", sans-serif; font-weight: 700; font-size: 25.5px; color: var(--white); white-space: nowrap; }
  .hero-copy { position: absolute; left: 42px; top: 97px; width: 270px; font-size: 8.6px; line-height: 13.5px; color: #ddd; }
  .hero-btn { position: absolute; left: 42px; top: 144px; padding: 0 12px; height: 23px; line-height: 23px; border-radius: 3px;
              background: linear-gradient(var(--magenta-light), var(--magenta)); color: var(--white); font-family: "Ubuntu", sans-serif; font-weight: 500; font-size: 9.5px; }
  .hero-dots { position: absolute; left: 42px; top: 181px; display: flex; gap: 3px; }
  .hero-dots i { width: 6px; height: 6px; border-radius: 50%; background: var(--white); }
  .hero-dots i:first-child { background: var(--magenta); }

  /* feature cards */
  .card { top: 390px; width: 169px; height: 127px; border: 1px solid #ddd; border-radius: 3px; background: var(--white); box-shadow: 0 1px 2px rgba(0,0,0,.08); }
  .card-photo { position: absolute; left: 12px; top: 12px; width: 144px; height: 79px; }
  .card-title { position: absolute; left: 12px; top: 98px; font-family: "Ubuntu", sans-serif; font-size: 13.5px; color: var(--magenta-light); }

  /* columns */
  .col { top: 560px; }
  .col h2 { font-family: "Ubuntu", sans-serif; font-weight: 400; font-size: 16px; color: var(--ink); margin-bottom: 12px; white-space: nowrap; }
  .col p { font-size: 8.5px; line-height: 15.2px; color: var(--text); margin-bottom: 7px; }
  .col-rule { top: 562px; width: 1px; height: 172px; background: linear-gradient(transparent, var(--line) 20%, var(--line) 80%, transparent); }
  .blog-list { list-style: none; margin-top: -4px; }
  .blog-list li { font-size: 8.4px; color: var(--magenta); border-bottom: 1px solid #eee; height: 24px; line-height: 22px; white-space: nowrap; }
  .blog-list li:last-child { border-bottom: 0; }
  .divider { left: 48px; top: 758px; width: 705px; height: 22px; background: radial-gradient(ellipse at 50% 0, rgba(0,0,0,.08), transparent 70%); }

  /* case study */
  .case { left: 48px; top: 810px; width: 415px; }
  .case h2 { font-family: "Ubuntu", sans-serif; font-weight: 400; font-size: 16.5px; line-height: 21px; color: var(--ink); margin-bottom: 8px; }
  .case p { font-size: 8.6px; line-height: 15.2px; color: var(--text); margin-bottom: 7px; }
  .video { left: 486px; top: 809px; width: 264px; height: 166px; border: 1px solid #ddd; padding: 5px; background: var(--white); }
  .video-frame { position: relative; width: 100%; height: 100%; background: linear-gradient(110deg, #1b1f3a 0%, #2c3560 45%, #151515 70%, #0c0c0c); }
  .video-play { position: absolute; left: 111px; top: 63px; }
  .video-caption { position: absolute; right: 6px; bottom: 8px; text-align: left; color: var(--white); font-family: "Ubuntu", sans-serif; }
  .video-caption b { display: block; font-weight: 500; font-size: 14px; }
  .video-caption span { font-size: 10px; }

  /* client strip */
  .client { top: 1030px; width: 92px; margin-left: -46px; text-align: center; font-family: "Ubuntu", sans-serif; font-weight: 500; font-size: 13px; color: #444; }

  /* footer */
  .footer { left: 0; top: 1082px; width: 799px; height: 118px; background: var(--footer); }
  .footer-nav { position: absolute; left: 52px; top: 30px; font-family: "Ubuntu", sans-serif; font-size: 10.5px; color: var(--white); }
  .footer-nav span { margin: 0 4px; }
  .footer-copy { position: absolute; left: 52px; top: 53px; font-size: 8.6px; color: #999; }
  .social { position: absolute; left: 640px; top: 29px; display: flex; gap: 3px; }
  .social i { width: 24px; height: 24px; border-radius: 50%; background: #e9e9e9; }
</style>
</head>
<body>

<header>
  <div class="abs brand"><span class="brand-mark"></span><span class="brand-name">plovK</span></div>
  <div class="abs brand-rule"></div>
  <div class="abs tagline">Creating Brand Champions</div>
  <nav class="abs nav">
    <a class="active">Home</a><a>About Us</a><a>Solutions</a><a>Resources</a><a>Our Work</a><a>Social Blog</a>
  </nav>
</header>

<section class="abs hero">
  <div class="hero-photo" role="img" aria-label="Group of cheering people stacking hands together"></div>
  <div class="hero-kicker">Sponsor Events</div>
  <div class="hero-title">and Social Media KPIs</div>
  <p class="hero-copy">Mauris vel lacus vitae felis vestibulum volutpat. Etiam est nunc, venenatis in, tristique eu, imperdiet ac, nisl. Cum sociis natoque penatibus et magnis dis parturient montes</p>
  <div class="hero-btn">Reqest a Demo</div>
  <div class="hero-dots"><i></i><i></i><i></i><i></i></div>
</section>

<section>
  <div class="abs card" style="left:48px"><div class="card-photo" role="img" aria-label="Excited sports fans in yellow" style="background:linear-gradient(135deg,#d7a23a,#c6412e 60%,#6b4b3a)"></div><div class="card-title">Amplify your Event</div></div>
  <div class="abs card" style="left:228px"><div class="card-photo" role="img" aria-label="Young friends walking in a city plaza" style="background:linear-gradient(135deg,#b9c3c8,#a78f7a 55%,#6b5a52)"></div><div class="card-title">Connect Venues</div></div>
  <div class="abs card" style="left:409px"><div class="card-photo" role="img" aria-label="Fans waving red flags in a stadium" style="background:linear-gradient(135deg,#5a6c56,#a3383a 50%,#cfc6b8)"></div><div class="card-title">In Action</div></div>
  <div class="abs card" style="left:590px"><div class="card-photo" role="img" aria-label="Large diverse crowd of smiling people" style="background:linear-gradient(135deg,#c9b3a3,#8d7a70 50%,#5c6f8a)"></div><div class="card-title">Social Solutions</div></div>
</section>

<section>
  <div class="abs col" style="left:52px;width:212px">
    <h2>What We Do</h2>
    <p>plovK is in the business of creating brand champions. We help get consumers to put your branded content into their Friendwall News Feed and Chirpline stream while attending live events.</p>
    <p>It is product placement in social media and the most scalable form of word-of-mouth advertising. We facilitate the posts by providing a platform that connects to photobooths, roving photographers, Like boxes, games and buzz walls</p>
  </div>
  <div class="abs col-rule" style="left:278px"></div>
  <div class="abs col" style="left:298px;width:212px">
    <h2>Why Customer Choose Us</h2>
    <p>Turn live audiences into brand champions.</p>
    <p>Global consumer brands engage plovK to leverage an asset they encounter at every event: attendees. Event guests have social network audiences who like and trust them. plovK solutions facilitate participation and enable easy distribution of branded content to friends. Fun for guests. Amplification for brands.</p>
  </div>
  <div class="abs col-rule" style="left:520px"></div>
  <div class="abs col" style="left:542px;width:210px">
    <h2>Social Blog Post</h2>
    <ul class="blog-list">
      <li>What does Harlstedt do for Social Media Today?</li>
      <li>Who is using Social Media? Young? Old? Both? Yes!</li>
      <li>Social Media Vista Summit Interview:</li>
      <li>RFID Connects Social Media to the Real World..</li>
      <li>Adding Experiential Social Media to Events</li>
    </ul>
  </div>
  <div class="abs divider"></div>
</section>

<section>
  <div class="abs case">
    <h2>Orvanta Amplifies Grand Circuit with RFID using<br>Social Media Technology</h2>
    <p>The video below shows how auto brands are connecting auto show and lifestyle event guests directly to social media using RFID and NFC Technology. These activations are fun for guests and expand the potential audience for social engagement beyond attendees to include their social network friends. Watch Video Below to see it in</p>
    <p>Duis tincidunt lectus quis dui viverra vestibulum. Suspendisse vulputate aliquam dui. Nulla elementum dui ut augue. Aliquam vehicula mi at mauris. Maecenas placerat, nisl at consequat rhoncus, sem nunc gravida justo, quis eleifend arcu velit quis lacus.</p>
  </div>
  <div class="abs video">
    <div class="video-frame" role="img" aria-label="Video still of a race car beside a presenter">
      <svg class="video-play" width="30" height="30" viewBox="0 0 30 30"><circle cx="15" cy="15" r="13" fill="rgba(0,0,0,.35)" stroke="#fff" stroke-width="2"/><path d="M12 9.5 L21 15 L12 20.5 Z" fill="#fff"/></svg>
      <div class="video-caption"><b>DANE HOLLOWAY</b><span>plovK CMO</span></div>
    </div>
  </div>
</section>

<section>
  <svg class="abs" style="left:74px;top:1027px" width="14" height="26" viewBox="0 0 14 26"><path d="M12 2 L2 13 L12 24" fill="none" stroke="#aaa" stroke-width="2"/></svg>
  <div class="abs client" style="left:146px">ORVANTA</div>
  <div class="abs client" style="left:246px">Velmora</div>
  <div class="abs client" style="left:338px">KAZURO</div>
  <div class="abs client" style="left:432px">Pixelmo</div>
  <div class="abs client" style="left:530px">Brellow</div>
  <div class="abs client" style="left:624px">dealnest</div>
  <svg class="abs" style="left:694px;top:1027px" width="14" height="26" viewBox="0 0 14 26"><path d="M2 2 L12 13 L2 24" fill="none" stroke="#aaa" stroke-width="2"/></svg>
</section>

<footer class="abs footer">
  <div class="footer-nav">Home<span>|</span>About Us<span>|</span>Solutions<span>|</span>Resources<span>|</span>Our Work<span>|</span>Social Blog</div>
  <div class="footer-copy">© 2013 Company Name.&nbsp; All right reserved.&nbsp; Term of Use</div>
  <div class="social"><i></i><i></i><i></i><i></i></div>
</footer>

</body>
</html>
```